Brindle Tides Boat Business Website

I would like a website that looks fresh, fun and exciting with great colors and photos of people having fun sailing and power boating. Current web page is www.brindletides.example. I want to be able to change content and photos myself once completed. Also needs to have customized info request forms and access to enrollment forms. Should work across all browsers and platforms including iPad and Mac. I have three product lines...instruction, charters and trips. See also keelhour.example/new-york, and facebook.com/brindletides, /keelhournewyork and /conchlagoonbar.
Updates

Reason: We are reviewing the designs submitted and will provide feedback asap. Thank you.

Industry/Entity Type

Business

Requirements
Must have
• self management/content management
form submissions
color, fun, excitement
links pages
photo pages
Nice to have
• calendar/class scheduling
guest book
visitor uploadable photos

```html
<!DOCTYPE html>
<html lang="en">
<head>
<meta charset="utf-8">
<title>Brindle Tides Charter Co. &amp; Nautical School</title>
<link href="https://fonts.googleapis.com/css2?family=Source+Sans+3:wght@300;400;600&display=swap" rel="stylesheet">
<style>
:root{
  --navy:#0d4a7a;
  --navy-dark:#0b3f68;
  --teal:#17998a;
  --teal-cal:#1fa896;
  --orange:#f0641e;
  --orange-btn:#f7921e;
  --sky:#5bb3e0;
  --grey-text:#6d6d6d;
  --grey-line:#d6d6d6;
  --body-text:#1d5a8c;
}
*{margin:0;padding:0;box-sizing:border-box}
html,body{width:842px;height:1200px;overflow:hidden;background:#fff}
body{font-family:"Source Sans 3",Arial,sans-serif;color:var(--body-text);position:relative}
.site{position:relative;width:842px;height:1200px;overflow:hidden}

/* header */
.site-header{position:absolute;left:0;top:0;width:842px;height:114px;background:linear-gradient(#fff 70%,#e8f1f8)}
.brand-name{position:absolute;left:48px;top:56px;font-size:27px;font-weight:400;color:var(--teal);letter-spacing:1px;line-height:1}
.brand-sub{position:absolute;left:48px;top:80px;font-size:10px;font-weight:400;color:var(--teal);letter-spacing:1.2px}
.social{position:absolute;left:624px;top:28px;display:flex;gap:5px}
.social span{width:15px;height:15px;border-radius:50%;background:var(--navy)}
.signup{position:absolute;left:684px;top:20px;width:108px;height:30px;background:var(--orange-btn);color:#fff;font-size:13px;line-height:30px;text-align:center}
.main-nav{position:absolute;right:52px;top:74px;display:flex;font-size:14px}
.main-nav a{color:var(--navy);text-decoration:none;padding:0 11px;border-left:1px solid #c9d3dc;line-height:18px}
.main-nav a:first-child{border-left:none}
.main-nav a:last-child{padding-right:0}

/* hero */
.hero{position:absolute;left:0;top:114px;width:842px;height:320px;background:var(--navy-dark)}
.hero-photo{position:absolute;left:34px;top:0;width:775px;height:320px;background:linear-gradient(#c9cfd4 0%,#a8a39c 45%,#9c3a34 65%,#8b9096 80%,#a5a9ab 100%)}
.hero-dots{position:absolute;left:396px;top:301px;display:flex;gap:3px}
.hero-dots span{width:9px;height:9px;border-radius:50%;background:#fff}
.hero-dots span:first-child{background:var(--navy)}

/* welcome */
.welcome h1{position:absolute;left:51px;top:466px;font-size:21px;font-weight:400;line-height:25px;color:var(--navy)}
.welcome-photo{position:absolute;left:44px;top:528px;width:160px;height:168px;border:1px solid #e2e2e2;border-radius:8px;padding:5px;background:#fff;box-shadow:0 1px 3px rgba(0,0,0,.1)}
.welcome-photo div{width:100%;height:100%;border-radius:6px;background:linear-gradient(#a9c7dd,#dfe4e8 45%,#7b7c74 75%,#4e5550)}
.welcome-text{position:absolute;left:218px;top:528px;width:352px}
.welcome-text .lead{font-size:12.5px;line-height:16px;margin-bottom:8px;font-weight:400}
.welcome-text p{font-size:10.6px;line-height:16.6px;font-weight:400;color:var(--body-text);margin-bottom:7px}

/* calendar */
.schedule h2{position:absolute;left:595px;top:466px;font-size:19px;font-weight:400;color:var(--orange)}
.calendar{position:absolute;left:596px;top:497px;width:196px;border:1px solid var(--grey-line);font-size:11.5px}
.cal-head{height:29px;background:var(--navy-dark);color:#fff;text-align:center;line-height:29px;font-size:14px;position:relative;border-radius:3px 3px 0 0}
.cal-head .prev,.cal-head .next{position:absolute;top:11px;width:0;height:0;border-top:4px solid transparent;border-bottom:4px solid transparent}
.cal-head .prev{left:12px;border-right:5px solid #fff}
.cal-head .next{right:12px;border-left:5px solid #fff}
.cal-days,.cal-grid{display:grid;grid-template-columns:repeat(7,1fr)}
.cal-days{background:var(--teal-cal);color:#fff;font-size:10px;height:18px;line-height:18px;text-align:center}
.cal-grid span{height:22px;line-height:22px;text-align:center;color:#333;border-right:1px solid #e4e4e4;border-bottom:1px solid #e4e4e4}
.cal-grid span:nth-child(7n){border-right:none}
.cal-grid .muted{color:#b4b4b4}
.cal-grid .today{background:#222;color:#fff}

.divider{position:absolute;left:58px;top:745px;width:736px;height:1px;background:#dcdcdc}

/* features */
.feature{position:absolute;top:778px;width:227px}
.feature h3{font-size:19px;font-weight:400;color:var(--teal);margin-left:4px;margin-bottom:6px}
.feature-photo{height:104px;border-radius:2px 2px 0 0;clip-path:path("M0 0H227V96Q170 104 110 99Q55 94 0 104Z")}
.feature h4{font-size:13.5px;font-weight:300;color:#333;margin:8px 0 4px 3px}
.feature p{width:212px;font-size:10px;line-height:16.5px;font-weight:300;color:var(--grey-text);margin-left:3px}
.feature .more{display:inline-flex;align-items:center;gap:4px;font-size:10px;color:var(--navy);margin:6px 0 0 3px;text-decoration:none}
.feature .more::after{content:"";border-top:3.5px solid transparent;border-bottom:3.5px solid transparent;border-left:4px solid var(--navy)}
.f-adv{left:50px}.f-adv .feature-photo{background:linear-gradient(#9cc6e6,#b9a48e 55%,#d9cdb6)}
.f-class{left:308px}.f-class .feature-photo{background:linear-gradient(#cfe1ee,#6a94b2 50%,#2e4b63)}
.f-quote{left:565px}.f-quote .feature-photo{background:linear-gradient(#c7d5de,#b54a48 50%,#dfe5ea)}

/* footer */
.footer-band{position:absolute;left:0;top:1040px;width:842px;height:76px;background:linear-gradient(90deg,#d4ebf7 0%,#fbe0d0 45%,#e3e3e3 70%,#d4ebf7 100%);opacity:.8}
.footer-nav{position:absolute;left:0;top:1134px;width:842px;text-align:center;font-size:11.5px}
.footer-nav a{color:var(--navy);text-decoration:none;padding:0 7px;border-left:1px solid var(--navy)}
.footer-nav a:first-child{border-left:none}
.copyright{position:absolute;left:0;top:1162px;width:842px;text-align:center;font-size:9px;font-weight:300;color:var(--grey-text)}
</style>
</head>
<body>
<div class="site">
  <header class="site-header">
    <div class="brand-name">BRINDLE TIDES</div>
    <div class="brand-sub">CHARTER CO. &amp; NAUTICAL SCHOOL</div>
    <div class="social" aria-label="Social links"><span></span><span></span><span></span></div>
    <a class="signup">Sign Up Today</a>
    <nav class="main-nav">
      <a>Home</a><a>Nautical School</a><a>Charter Sailing</a><a>Adventure Travel</a><a>Contact Us</a>
    </nav>
  </header>

  <section class="hero">
    <div class="hero-photo" role="img" aria-label="Red fireboat cruising on the river in front of the city skyline"></div>
    <div class="hero-dots"><span></span><span></span><span></span><span></span><span></span></div>
  </section>

  <section class="welcome">
    <h1>Welcome to Brindle Tides Charter Co.<br>and Nautical School!</h1>
    <div class="welcome-photo"><div role="img" aria-label="White motorboat moored at a wooden dock"></div></div>
    <div class="welcome-text">
      <p class="lead">KeelHour New York is located at Wharfside Piers marina, in the heart of Manhattan.</p>
      <p>You don't have to drive your car for an hour or more in heavy traffic to enjoy your boat any more. You're only a subway stop or a taxi ride away. Join KeelHour and the happy few who can say they have a boat at Wharfside Piers. We offer memberships and charters on both sail and powerboats. Visit our floating office, the infamous Conch Lagoon located at Tideline 3 Marina, Wharfside Piers, Pier 59 or contact us via phone or email, we will be glad to give you more information.</p>
      <p>Look at our available boats, start dreaming about your summer…and then make this the summer you're hoping it will be!</p>
    </div>
  </section>

  <section class="schedule">
    <h2>Classing Schedule</h2>
    <div class="calendar">
      <div class="cal-head"><span class="prev"></span>MAY 2013<span class="next"></span></div>
      <div class="cal-days"><span>Su</span><span>Mo</span><span>Tu</span><span>We</span><span>Th</span><span>Fr</span><span>Sa</span></div>
      <div class="cal-grid">
        <span class="muted">28</span><span class="muted">29</span><span class="muted">30</span><span class="muted">31</span><span>1</span><span>2</span><span>3</span>
        <span>4</span><span>5</span><span>6</span><span>7</span><span>8</span><span>9</span><span>10</span>
        <span>11</span><span>12</span><span>13</span><span>14</span><span>15</span><span>16</span><span>17</span>
        <span>18</span><span>19</span><span class="today">20</span><span>21</span><span>22</span><span>23</span><span>24</span>
        <span>25</span><span>26</span><span>27</span><span>28</span><span>29</span><span>30</span><span class="muted">1</span>
        <span class="muted">2</span><span class="muted">3</span><span class="muted">4</span><span class="muted">5</span><span class="muted">6</span><span class="muted">7</span><span class="muted">8</span>
      </div>
    </div>
  </section>

  <div class="divider"></div>

  <article class="feature f-adv">
    <h3>Adventures &amp; Travel</h3>
    <div class="feature-photo" role="img" aria-label="Beachfront amusement park with ferris wheel and apartment towers"></div>
    <h4>Nunc tempus felis</h4>
    <p>Vivamus porttitor, g, purus nisi eleifend libero, a tempus libero lectus feugiat felis. Morbi diam mauris, viverra in, gravida eu</p>
    <a class="more">Learn More</a>
  </article>
  <article class="feature f-class">
    <h3>Classes &amp; Training</h3>
    <div class="feature-photo" role="img" aria-label="Student at the helm of a boat with the skyline across the water"></div>
    <h4>Nunc tempus felis</h4>
    <p>Vivamus porttitor, g, purus nisi eleifend libero, a tempus libero lectus feugiat felis. Morbi diam mauris, viverra in, gravida eu</p>
    <a class="more">Learn More</a>
  </article>
  <article class="feature f-quote">
    <h3>Request Quote</h3>
    <div class="feature-photo" role="img" aria-label="Crew member in a red shirt at a marina full of sailboats"></div>
    <h4>Nunc tempus felis</h4>
    <p>Vivamus porttitor, g, purus nisi eleifend libero, a tempus libero lectus feugiat felis. Morbi diam mauris, viverra in, gravida eu</p>
    <a class="more">Learn More</a>
  </article>

  <div class="footer-band" role="img" aria-label="Decorative blue, orange and grey wave ribbons above the footer"></div>

  <nav class="footer-nav">
    <a>Home</a><a>Nautical School</a><a>Charter Sailing</a><a>Adventure Travel</a><a>Charter Power</a><a>Our Captain</a><a>Sitemap</a><a>Contact Us</a>
  </nav>
  <p class="copyright">Copyright © 2013 Company Name.&nbsp; All right reserved.&nbsp; Term of Use</p>
</div>
</body>
</html>
```